LITTLE DESIGN WORK REQUIRED!

UPDATE: WE WEREN'T OVERLY ECSTATIC WITH THE DESIGNS WE WERE RECEIVING SO WE DID MOST OF THE DESIGN WORK OURSELVES...

PLEASE SEE THE NEWLY ATTACHED PPT DOC TO VIEW NEARLY EXACT REPLICAS OF WHAT WE WANT THE SITE TO LOOK LIKE. WE NOW NEED YOUR HELP TO MAKE IT LOOK LIKE SOMETHING WORTHY OF THE WEB.

NO CODING REQUIRED - EXPECTED OUTPUT PSD FILES

Hi everyone!

We're looking for a designer to work their magic for our site! We're a not-for-profit program aimed at helping young people realise their potential!

In the attached PPT file, you'll notice we've already DESIGNED THE ENTIRE SITE IN POWERPOINT. Now, we need YOU to make the small changes we requested in the document as well as design the whole thing in psd.

Any questions, don't hesitate to ask.

Brook-Rise
Updates

We've done about 95% of the design for you. Please fine-tune it. See the newly attached PPT doc for details. 

The best two designs will win. This project closes on Friday - please message us if you are absolutely sure you cannot make the deadline.

Thanks,
Brook-Rise

```html
<!DOCTYPE html>
<html lang="en">
<head>
<meta charset="utf-8">
<title>Brook-Rise · Feats</title>
<link rel="stylesheet" href="https://fonts.googleapis.com/css2?family=Arimo:ital,wght@0,400;0,700;1,400;1,700&display=swap">
<style>
  :root {
    --backdrop: #b9b9b9;
    --page: #f7f7f7;
    --ink: #4a4a4a;
    --quote: #8c8c8c;
    --heading: #173d0c;
    --caption: #1f3d12;
    --nav: #2b2b2b;
    --nav-edge: #151515;
    --accent: #7bb800;
    --accent-dark: #4f8a00;
    --footer: #1e1e1e;
    --footer-text: #e6e6e6;
    --field: #fafafa;
    --sky: #3f66b8;
    --grass: #6f8f2a;
    --swim-sky: #4d86c6;
    --skin: #b0683c;
    --red: #e10000;
    --red-dark: #a30000;
    --navy: #2c3f6b;
    --gold: #e7a800;
    --badge-text: #ffffff;
  }
  * { box-sizing: border-box; margin: 0; padding: 0; }
  html, body { width: 922px; height: 1200px; overflow: hidden; }
  body {
    position: relative;
    background: var(--backdrop);
    font-family: "Arimo", Arial, sans-serif;
    color: var(--ink);
  }
  .page {
    position: absolute; left: 56px; top: 0; width: 810px; height: 960px;
    background: linear-gradient(#ffffff, var(--page));
  }
  .abs { position: absolute; }

  .brand { left: 130px; top: 48px; display: flex; align-items: center; gap: 10px; }
  .brand-mark { width: 26px; height: 26px; border-radius: 50%; background: var(--accent); }
  .brand-name { font-size: 38px; font-weight: 700; color: #1a1a1a; letter-spacing: -1px; }

  .quote { left: 488px; top: 28px; width: 320px; text-align: center; color: var(--quote);
    font-size: 23px; font-style: italic; line-height: 22px; }
  .quote-author { left: 533px; top: 80px; color: var(--quote); font-size: 19px; }
  .share { left: 697px; top: 79px; width: 64px; height: 21px; background: #4a69a9;
    border-radius: 2px; display: flex; align-items: center; gap: 4px; padding-left: 4px;
    color: #fff; font-size: 9px; font-weight: 700; }
  .share-box { width: 12px; height: 12px; background: #fff; }

  .nav { left: 124px; top: 132px; display: flex; gap: 4px; }
  .nav-item { height: 55px; background: var(--nav); border: 1px solid var(--nav-edge);
    border-radius: 7px; color: #fff; font-size: 18px; display: flex; align-items: center;
    justify-content: center; box-shadow: 0 2px 3px rgba(0,0,0,.35); }
  .nav-item.is-active { background: linear-gradient(var(--accent), #5f9e00); border-color: #4b8000; }

  .title { left: 124px; top: 200px; font-size: 36px; font-weight: 700; font-style: italic; color: var(--heading); }
  .intro { left: 126px; top: 245px; width: 658px; font-size: 17.4px; line-height: 19px; color: #555; }

  .photo { box-shadow: 0 1px 3px rgba(0,0,0,.3); }
  .badge { color: var(--badge-text); text-align: center; display: flex; flex-direction: column;
    align-items: center; box-shadow: 0 1px 3px rgba(0,0,0,.3); }
  .badge-kili { justify-content: flex-end; padding-bottom: 40px; }
  .badge-kili .event-name { font-size: 31px; font-weight: 700; letter-spacing: -0.5px; line-height: 36px; }
  .badge-kili .event-year { font-size: 32px; font-weight: 700; line-height: 36px; }
  .badge-swim { justify-content: space-between; padding: 14px 0 10px; }
  .badge-swim .event-name { font-size: 42px; font-weight: 700; line-height: 40px; }
  .badge-swim .event-sub { font-size: 28px; font-style: italic; line-height: 28px; }
  .badge-swim .event-kind { font-size: 28px; font-weight: 700; font-style: italic; line-height: 30px; }
  .badge-swim .event-date { font-size: 27px; line-height: 30px; }
  .badge-swim sup { font-size: 15px; }

  .caption { font-size: 18px; font-style: italic; color: var(--caption); letter-spacing: 0.15px; }

  .footer { left: 0; top: 960px; width: 922px; height: 208px; background: var(--footer); }
  .footer-title { color: var(--footer-text); font-size: 17px; font-weight: 400; }
  .browse-links { left: 60px; top: 994px; list-style: none; color: var(--accent); font-size: 17px; line-height: 23px; }
  .field { background: var(--field); border: 1px solid #999; border-radius: 3px;
    font-size: 10px; color: #222; padding: 3px 4px; }
  .btn { background: linear-gradient(var(--accent), var(--accent-dark)); color: #fff;
    font-size: 12px; text-align: center; border-radius: 2px; line-height: 19px; }
  .social { width: 68px; height: 68px; border-radius: 12px; background: #f2f2f2;
    display: flex; align-items: center; justify-content: center; color: #333; font-size: 11px; font-weight: 700; }
  .signup { left: 758px; width: 99px; height: 52px; display: flex; align-items: center;
    justify-content: center; color: #fff; font-weight: 700; border: 1px solid #666; }
  .legal { left: 0; top: 1168px; width: 922px; height: 32px; background: var(--accent);
    color: #fff; font-size: 15px; text-align: right; padding: 7px 12px 0 0; }
</style>
</head>
<body>
  <div class="page"></div>

  <header>
    <div class="abs brand"><span class="brand-mark"></span><span class="brand-name">BROOK-RISE</span></div>
    <p class="abs quote">“What would you do if you knew you could not fail?”</p>
    <p class="abs quote-author">- R. Halloran</p>
    <div class="abs share"><span class="share-box"></span>SHARE</div>
  </header>

  <nav class="abs nav">
    <a class="nav-item" style="width:72px">Home</a>
    <a class="nav-item" style="width:112px">About us</a>
    <a class="nav-item" style="width:120px">Resources</a>
    <a class="nav-item" style="width:127px">Workshops</a>
    <a class="nav-item" style="width:149px">Ambassadors</a>
    <a class="nav-item is-active" style="width:72px">Feats</a>
  </nav>

  <main>
    <h1 class="abs title">Feats</h1>
    <p class="abs intro">Brook-Rise feats are a set of challenges we set ourselves to help raise funds for the program, test our limits, and discover our own potential. Whether it may be running a marathon, building a school, or climbing one of the Seven Summits, we encourage as many participants as possible to get involved. Recommend a Feat on our Chatterbox page.</p>

    <div class="abs photo" role="img" aria-label="Snow-capped mountain above a savanna with elephants walking across the grass"
      style="left:124px;top:361px;width:441px;height:231px;background:linear-gradient(#8fb0e0 0%, var(--sky) 45%, #27408f 62%, var(--grass) 78%, #88a83a 100%)"></div>
    <div class="abs badge badge-kili" aria-label="Kilimanjaro 2013 event badge"
      style="left:573px;top:361px;width:221px;height:231px;background:linear-gradient(var(--accent), #3f7a00)">
      <span class="event-name">KILIMANJARO</span>
      <span class="event-year">2013</span>
    </div>
    <p class="abs caption" style="left:127px;top:598px">More details to come. Like us on Chatterbox to keep in touch!</p>

    <div class="abs photo" role="img" aria-label="Swimmer seen from behind pulling on a yellow swim cap against a blue sky"
      style="left:124px;top:642px;width:441px;height:231px;background:linear-gradient(var(--swim-sky) 0%, #6c9fd6 55%, var(--skin) 75%, #8f4f2b 100%)"></div>
    <div class="abs badge badge-swim" aria-label="Shore Classic Ocean Swim event badge"
      style="left:572px;top:642px;width:221px;height:231px;background:linear-gradient(var(--red), var(--red-dark))">
      <div><div class="event-name">SHORE</div><div class="event-sub">Classic</div></div>
      <div class="event-kind">Ocean Swim</div>
      <div class="event-date">2<sup>nd</sup> Feb 2013</div>
    </div>
    <p class="abs caption" style="left:127px;top:883px">More details to come. Like us on Chatterbox to keep in touch!</p>
  </main>

  <footer>
    <div class="abs footer"></div>
    <h2 class="abs footer-title" style="left:60px;top:972px">Browse</h2>
    <ul class="abs browse-links">
      <li>&gt;Home</li><li>&gt;About us</li><li>&gt;Resources</li><li>&gt;Workshops</li><li>&gt;Ambassadors</li><li>&gt;Feats</li>
    </ul>

    <h2 class="abs footer-title" style="left:245px;top:972px">Search</h2>
    <div class="abs field" style="left:245px;top:1000px;width:227px;height:19px;padding:1px 4px">
      <svg width="14" height="14" viewBox="0 0 14 14"><circle cx="8" cy="6" r="4" fill="none" stroke="#555" stroke-width="1.5"/><line x1="5" y1="9" x2="1" y2="13" stroke="#555" stroke-width="2"/></svg>
    </div>
    <div class="abs btn" style="left:245px;top:1026px;width:64px;height:19px">Search</div>
    <h2 class="abs footer-title" style="left:243px;top:1056px">Follow Us</h2>
    <div class="abs social" style="left:247px;top:1085px">Chatterbox</div>
    <div class="abs social" style="left:334px;top:1085px">Streamly</div>

    <h2 class="abs footer-title" style="left:501px;top:972px">Contact Us</h2>
    <div class="abs field" style="left:501px;top:999px;width:227px;height:19px">Name:</div>
    <div class="abs field" style="left:501px;top:1026px;width:227px;height:19px">Email:</div>
    <div class="abs field" style="left:501px;top:1052px;width:227px;height:68px">Message:</div>
    <div class="abs btn" style="left:501px;top:1131px;width:63px;height:18px">Send</div>

    <h2 class="abs footer-title" style="left:754px;top:972px">Sign Up</h2>
    <div class="abs signup" style="top:997px;background:var(--accent);font-size:22px">FEATS</div>
    <div class="abs signup" style="top:1052px;background:var(--navy);font-size:12px">Ambassadors</div>
    <div class="abs signup" style="top:1108px;background:var(--gold);font-size:14px">WORKSHOPS</div>

    <p class="abs legal">@ 2012 Brook-Rise&nbsp; All Rights Reserved</p>
  </footer>
</body>
</html>
```